Smile club flyer design

I am launching an office smile club and would like a design that sits my branding and that is appealing to customers. I have a design (I need a new one) that has all the information.
My website is maplecrestdentalcaretn.example
Brand color is green. The design can be any color

Target Market(s)

Ages 30+

Industry/Entity Type

Dental

Font styles to use
Serif

Requirements
Must have
• Appealing to patients

```html
<!DOCTYPE html>
<html lang="en">
<head>
<meta charset="utf-8">
<title>Smile Club Membership – Maplecrest Dental Care</title>
<link rel="stylesheet" href="https://fonts.googleapis.com/css2?family=Archivo:wght@800;900&family=Figtree:ital,wght@0,400;0,500;0,600;0,700;0,800;1,400&family=Great+Vibes&family=Playfair+Display:wght@700&display=swap">
<style>
  :root{
    --backdrop:#231f20;
    --mint:#dcf5ef;
    --green:#3a8140;
    --teal:#52b7a8;
    --gold:#bf9f68;
    --ink:#1f2a24;
    --white:#ffffff;
    --line:#cfe6df;
  }
  *{box-sizing:border-box;margin:0;padding:0}
  html,body{width:917px;height:1200px;overflow:hidden;background:var(--backdrop)}
  body{font-family:"Figtree",sans-serif;color:var(--ink)}
  .flyer{position:absolute;left:97px;top:88px;width:723px;height:1022px;background:var(--mint);overflow:hidden}
  .abs{position:absolute}
  .brand{left:0;right:0;top:54px;text-align:center;font-family:"Playfair Display",serif;font-weight:700;font-size:32px;color:var(--green)}
  .intro{left:0;right:0;top:112px;text-align:center;font-family:"Great Vibes",cursive;font-size:52px;color:var(--ink)}
  .headline{left:0;right:0;top:170px;text-align:center;font-family:"Archivo",sans-serif;font-weight:900;font-size:84px;line-height:1;letter-spacing:-3px;color:var(--gold)}
  .membership{left:0;right:0;top:245px;text-align:center;font-family:"Figtree",sans-serif;font-weight:500;font-size:31px;letter-spacing:15px;padding-left:15px;color:var(--ink);line-height:1}
  .band{left:69px;width:581px;height:34px;color:var(--white);font-weight:500;font-size:27px;text-align:center;line-height:34px;letter-spacing:-.3px}
  .band--green{top:292px;background:linear-gradient(90deg,rgba(58,129,64,0),var(--green) 30%,var(--green) 70%,rgba(58,129,64,0))}
  .band--teal{top:328px;background:linear-gradient(90deg,rgba(82,183,168,0),var(--teal) 30%,var(--teal) 70%,rgba(82,183,168,0))}
  .plan{top:389px;width:189px;height:312px;background:var(--white);border-radius:10px;border:1px solid var(--line);box-shadow:0 3px 8px rgba(30,80,60,.12);overflow:hidden}
  .plan--core{left:64px}.plan--bright{left:267px}.plan--total{left:480px}
  .plan__head{height:60px;color:var(--white);text-align:center;padding-top:15px}
  .plan__wave{display:block;width:189px;height:14px}
  .plan__title{font-weight:700;font-size:21px;line-height:1}
  .plan__sub{font-weight:400;font-size:15px;line-height:1;margin-top:3px}
  .plan--core .plan__head,.plan--total .plan__head{background:var(--green)}
  .plan--bright .plan__head{background:var(--teal)}
  .plan__list{list-style:none;position:absolute;left:22px;right:6px;top:85px}
  .plan__list li{position:relative;padding-left:22px;font-size:13.5px;line-height:16px;margin-bottom:11px}
  .plan__list svg{position:absolute;left:0;top:1px;width:14px;height:14px}
  .plan__rule{position:absolute;left:20px;right:20px;top:257px;height:1px}
  .plan__price{position:absolute;left:0;right:0;top:263px;text-align:center;font-weight:700;font-size:29px;line-height:1}
  .plan__price span{font-weight:400;font-size:20px}
  .plan--core .plan__rule,.plan--total .plan__rule{background:var(--green)}
  .plan--bright .plan__rule{background:var(--teal)}
  .plan--core .plan__price,.plan--total .plan__price{color:var(--green)}
  .plan--bright .plan__price{color:var(--teal)}
  .why__title{left:65px;top:732px;font-weight:800;font-size:19px;color:var(--green)}
  .why__list{left:64px;top:759px;list-style:none}
  .why__list li{display:flex;align-items:center;height:25.5px;font-size:14px}
  .why__icon{width:22px;height:22px;border-radius:50%;background:var(--teal);margin-right:12px;display:flex;align-items:center;justify-content:center}
  .refresh{left:267px;top:733px;width:392px;height:117px;background:var(--white);border-radius:8px;border:1px solid #efe5d4;overflow:hidden;box-shadow:0 3px 8px rgba(30,80,60,.1)}
  .refresh__shape{position:absolute;left:0;top:0;width:180px;height:117px}
  .refresh__tag{position:absolute;left:15px;top:0;width:68px;height:20px;background:var(--green);color:var(--white);font-size:13px;line-height:20px;padding-left:15px;border-radius:0 0 0 0 ;border-top-right-radius:10px}
  .refresh__name{position:absolute;left:19px;top:30px;color:var(--white);font-weight:700;font-size:21px;line-height:1}
  .refresh__sub{position:absolute;left:19px;top:50px;color:var(--white);font-size:14.5px;letter-spacing:-.3px}
  .refresh__price{position:absolute;left:19px;top:70px;color:var(--white);font-weight:800;font-size:31px;line-height:1}
  .refresh__list{position:absolute;left:186px;top:28px;list-style:none}
  .refresh__list li{position:relative;padding-left:21px;font-size:13.5px;line-height:16px;margin-bottom:11px}
  .refresh__list svg{position:absolute;left:0;top:1px;width:14px;height:14px}
  .join{left:64px;top:886px;width:290px;height:104px;background:var(--white);border-radius:8px;border:1px solid var(--line);box-shadow:0 3px 8px rgba(30,80,60,.1)}
  .join__title{position:absolute;left:15px;top:26px;font-weight:700;font-size:17px}
  .join__phone{position:absolute;left:11px;top:50px;display:flex;align-items:center;font-weight:800;font-size:32px;color:var(--green);letter-spacing:-.5px}
  .join__phone svg{width:27px;height:27px;margin-right:8px}
  .finance__title{left:371px;top:883px;font-weight:700;font-size:16px}
  .partner{top:909px;height:37px;background:var(--white);display:flex;align-items:center;justify-content:center;font-weight:700;font-size:21px;color:#2d5a4e}
  .partner--fund{left:371px;width:148px}
  .partner--plum{left:527px;width:132px}
  .partner i{width:12px;height:12px;border-radius:50%;background:#2d5a4e;margin-right:7px;display:block}
  .finance__note{left:371px;top:952px;font-size:14px}
  .finance__fee{left:371px;top:976px;font-size:10px;font-style:italic}
  .footbar{left:0;right:0;bottom:0;height:7px;background:var(--green)}
</style>
</head>
<body>
<main class="flyer">
  <div class="abs brand">Maplecrest Dental Care</div>
  <div class="abs intro">Introducing</div>
  <h1 class="abs headline">SMILE CLUB</h1>
  <div class="abs membership">MEMBERSHIP</div>
  <div class="abs band band--green">AFFORDABLE DENTAL CARE</div>
  <div class="abs band band--teal">NO INSURANCE REQUIRED</div>

  <section class="abs plan plan--core">
    <div class="plan__head"><div class="plan__title">CORE CARE</div><div class="plan__sub">PREVENTIVE</div></div>
    <svg class="plan__wave" viewBox="0 0 189 14" preserveAspectRatio="none"><path d="M0 0H189V2Q94.5 20 0 2Z" fill="#3a8140"/></svg>
    <ul class="plan__list">
      <li><svg viewBox="0 0 14 14"><circle cx="7" cy="7" r="7" fill="#3a8140"/><path d="M4 7.2l2 2 4-4" stroke="#fff" stroke-width="1.6" fill="none"/></svg>Comprehensive<br>Annual Exam</li>
      <li><svg viewBox="0 0 14 14"><circle cx="7" cy="7" r="7" fill="#3a8140"/><path d="M4 7.2l2 2 4-4" stroke="#fff" stroke-width="1.6" fill="none"/></svg>2 Professional<br>Cleanings per Year</li>
      <li><svg viewBox="0 0 14 14"><circle cx="7" cy="7" r="7" fill="#3a8140"/><path d="M4 7.2l2 2 4-4" stroke="#fff" stroke-width="1.6" fill="none"/></svg>Routine Bitewing<br>X-rays</li>
      <li><svg viewBox="0 0 14 14"><circle cx="7" cy="7" r="7" fill="#3a8140"/><path d="M4 7.2l2 2 4-4" stroke="#fff" stroke-width="1.6" fill="none"/></svg>10% Savings on<br>Treatment</li>
    </ul>
    <div class="plan__rule"></div>
    <div class="plan__price">$39<span>/month</span></div>
  </section>

  <section class="abs plan plan--bright">
    <div class="plan__head"><div class="plan__title">BRIGHT</div><div class="plan__sub">COSMETIC</div></div>
    <svg class="plan__wave" viewBox="0 0 189 14" preserveAspectRatio="none"><path d="M0 0H189V2Q94.5 20 0 2Z" fill="#52b7a8"/></svg>
    <ul class="plan__list">
      <li><svg viewBox="0 0 14 14"><circle cx="7" cy="7" r="7" fill="#52b7a8"/><path d="M4 7.2l2 2 4-4" stroke="#fff" stroke-width="1.6" fill="none"/></svg>Annual In-Office<br>Whitening<br>(Top &amp; Bottom)</li>
      <li><svg viewBox="0 0 14 14"><circle cx="7" cy="7" r="7" fill="#52b7a8"/><path d="M4 7.2l2 2 4-4" stroke="#fff" stroke-width="1.6" fill="none"/></svg>Custom Whitening<br>Trays</li>
      <li><svg viewBox="0 0 14 14"><circle cx="7" cy="7" r="7" fill="#52b7a8"/><path d="M4 7.2l2 2 4-4" stroke="#fff" stroke-width="1.6" fill="none"/></svg>15% Savings on<br>Elective Treatment</li>
    </ul>
    <div class="plan__rule"></div>
    <div class="plan__price">$59<span>/month</span></div>
  </section>

  <section class="abs plan plan--total">
    <div class="plan__head"><div class="plan__title">TOTAL SMILE</div><div class="plan__sub">PERIODONTAL</div></div>
    <svg class="plan__wave" viewBox="0 0 189 14" preserveAspectRatio="none"><path d="M0 0H189V2Q94.5 20 0 2Z" fill="#3a8140"/></svg>
    <ul class="plan__list" style="left:15px">
      <li><svg viewBox="0 0 14 14"><circle cx="7" cy="7" r="7" fill="#3a8140"/><path d="M4 7.2l2 2 4-4" stroke="#fff" stroke-width="1.6" fill="none"/></svg>3-4 Perio Maintenance<br>Visits per Year</li>
      <li><svg viewBox="0 0 14 14"><circle cx="7" cy="7" r="7" fill="#3a8140"/><path d="M4 7.2l2 2 4-4" stroke="#fff" stroke-width="1.6" fill="none"/></svg>1 Comprehensive<br>Exam</li>
      <li><svg viewBox="0 0 14 14"><circle cx="7" cy="7" r="7" fill="#3a8140"/><path d="M4 7.2l2 2 4-4" stroke="#fff" stroke-width="1.6" fill="none"/></svg>Diagnostic X-rays</li>
      <li><svg viewBox="0 0 14 14"><circle cx="7" cy="7" r="7" fill="#3a8140"/><path d="M4 7.2l2 2 4-4" stroke="#fff" stroke-width="1.6" fill="none"/></svg>15% Savings on<br>Restorative &amp;<br>Elective Care</li>
    </ul>
    <div class="plan__rule"></div>
    <div class="plan__price">$89<span>/month</span></div>
  </section>

  <h2 class="abs why__title">WHY JOIN?</h2>
  <ul class="abs why__list">
    <li><span class="why__icon"><svg width="12" height="12" viewBox="0 0 12 12"><path d="M2.5 6.2l2.3 2.3 4.7-4.8" stroke="#fff" stroke-width="1.5" fill="none"/></svg></span>No insurance required</li>
    <li><span class="why__icon"><svg width="12" height="12" viewBox="0 0 12 12"><path d="M2.5 6.2l2.3 2.3 4.7-4.8" stroke="#fff" stroke-width="1.5" fill="none"/></svg></span>Immediate savings</li>
    <li><span class="why__icon"><svg width="12" height="12" viewBox="0 0 12 12"><path d="M2.5 6.2l2.3 2.3 4.7-4.8" stroke="#fff" stroke-width="1.5" fill="none"/></svg></span>Transparent pricing</li>
    <li><span class="why__icon"><svg width="12" height="12" viewBox="0 0 12 12"><path d="M2.5 6.2l2.3 2.3 4.7-4.8" stroke="#fff" stroke-width="1.5" fill="none"/></svg></span>Family-friendly</li>
  </ul>

  <section class="abs refresh">
    <svg class="refresh__shape" viewBox="0 0 180 117" preserveAspectRatio="none"><path d="M0 0H160Q188 58 160 117H0Z" fill="#bf9f68"/></svg>
    <div class="refresh__tag">NEW</div>
    <div class="refresh__name">SMILE</div>
    <div class="refresh__sub">REFRESH PACKAGE</div>
    <div class="refresh__price">$499</div>
    <ul class="refresh__list">
      <li><svg viewBox="0 0 14 14"><circle cx="7" cy="7" r="7" fill="#bf9f68"/><path d="M4 7.2l2 2 4-4" stroke="#fff" stroke-width="1.6" fill="none"/></svg>Cleaning + Comprehensive<br>Exam + Whitening</li>
      <li><svg viewBox="0 0 14 14"><circle cx="7" cy="7" r="7" fill="#bf9f68"/><path d="M4 7.2l2 2 4-4" stroke="#fff" stroke-width="1.6" fill="none"/></svg>Limited Time Offer</li>
    </ul>
  </section>

  <section class="abs join">
    <div class="join__title">JOIN SMILE CLUB TODAY!</div>
    <div class="join__phone"><svg viewBox="0 0 28 28"><circle cx="14" cy="14" r="14" fill="#bf9f68"/><path d="M10 7.5c.8 0 1.5 2.2 1.7 3 .1.7-1.2 1.3-1 2 .6 1.8 2.3 3.6 4 4.3.7.3 1.4-1 2-.9.9.2 3 1 3 1.8 0 1.2-1.5 2.6-2.8 2.6C12.4 20.3 7.7 15.6 7.7 10.3 7.7 9 8.8 7.5 10 7.5z" fill="none" stroke="#fff" stroke-width="1.3"/></svg>865-555-0142</div>
  </section>

  <h3 class="abs finance__title">Flexible Financing for Treatment:</h3>
  <div class="abs partner partner--fund"><i></i>CareFund</div>
  <div class="abs partner partner--plum"><i></i>Plumly</div>
  <div class="abs finance__note">Payment Plans Available</div>
  <div class="abs finance__fee">*$49 Lifetime Activation Fee (Non-Refundable)</div>

  <div class="abs footbar"></div>
</main>
</body>
</html>
```